Programme Management Specialists based in London focused on providing a PMO service to run Business

We need a new wordpress design template that will allow us to populate the content using wordpress

1) We have logo and colour theme ( I will upload)

1) I needs it to be mobile optimised.

Proposition
We are an independent and technology agnostic programme office (PMO) providing highly specialised managed service capable of setting up & delivering large scale business transformation programmes as a result of digitalisation.

By setting up a temporary environment within your environment , we provide the required structure, processes and expertise to deliver company wide organisational & operational change as a consequence of digital innovation.

WE ARE NOT AN IT FIRM - BUT PROJECT MANAGEMENT FIRM. WE MANAGE ALL ELEMENTS OF THE PROJECT (IT, ECOMMECE, LOGISTICS, FINANCE, HR, SUPPLY CHAIN, CALL CENTRE, SHOPS) to ensure the right OUTCOME.

A LITTLE EXTRA:
We provide structure during change giving the confidence required during a period of uncertainty

INDUSTRY
RETAIL & MEDIA

Hi, I thought it may help if I mentioned a few other things I see us like a conductor of an orchestra - without is you have a bunch of talented musicians but no symphony. Also more depth about what we do: A little more background - The site Pages Wordpress website(non transactional) Build mobile first Blog section Proposition We are an independent and technology agnostic programme office (PMO) providing highly specialised managed service capable of setting up & delivering large scale business transformation programmes as a result of digitalisation. By setting up a temporary environment within your environment , we provide the required structure, processes and expertise to agressively deliver conpany wide organisational & operational change as a consequence of digital innovation. Extra 1)We provide structure during change giving the confidence required during a period of uncertainty 2) we are project management (not IT) Our signature KWR : Transforming your vision into reality Our Services 1. programme Management 2. Digital Transformation delivery consultancy 4. full PMO service(programme management, risk management, change management, communication strategy) 5. Audit exiting programmes - 6. RECOVERY - ensure programmes than have gone awry are put back on track. 7. Business process re-engineering Change often comes through execution, the key to our service is that throughout our engagement we work closely with your staff to embed a culture of perpetual change capable of delivering at pace your customers expects long after we leave. The Industries we target Retail Media Travel So why is this important to our clients: Our approach leads to efficiency and helps deliver projects even better, faster and cheaper. We educate organisations to understand that project management processes should be implemented consistently across the organization thus allowing true business transformation. Many companies give this responsibility to one or more people in a Project Management Office (PMO). There are many structures for a PMO and many types of services that we can offer. We help organization to firstly determine the services that are important to them and then create an overall approach to implementing. Since this is a culture change initiative, the effort can be time-consuming and difficult. However, the rewards are also large. We ensure the PMO is established with a clear vision, strong sponsorship and a solid approach, creating a vehicle for providing a tremendous amount of value for the company.

```html
<!DOCTYPE html>
<html lang="en">
<head>
<meta charset="utf-8">
<title>KWR Keystone Works</title>
<link rel="stylesheet" href="https://fonts.googleapis.com/css2?family=Arimo:wght@400;700&family=Pathway+Gothic+One&display=swap">
<style>
:root{
  --orange:#eda600;
  --ink:#111;
  --text:#333;
  --grey-band:#efefef;
  --footer:#3a3a3a;
  --white:#fff;
  --nav-active:#ececec;
}
*{box-sizing:border-box;margin:0;padding:0}
html,body{width:1047px;height:1200px;overflow:hidden;background:var(--white)}
body{position:relative;font-family:"Arimo",Arial,sans-serif;color:var(--text)}
.abs{position:absolute}
.display{font-family:"Pathway Gothic One","Oswald",sans-serif;font-weight:400}

/* header */
.brand{left:69px;top:22px;display:flex;align-items:center;gap:10px}
.brand-mark{font-size:52px;font-weight:700;color:var(--ink);letter-spacing:-2px;line-height:1}
.brand-divider{width:1px;height:64px;background:#ccc;margin:0 8px}
.brand-name{line-height:1}
.brand-name .l1{font-size:20px;font-weight:700;color:#333}
.brand-name .l2{font-size:20px;font-weight:700;color:var(--orange);margin-top:1px}
.brand-name .l3{font-size:7px;font-weight:700;color:#222;margin-top:5px}
.main-nav{left:483px;top:35px;display:flex;font-size:13px;font-weight:700;color:#333}
.main-nav a{display:block;height:36px;line-height:36px;text-decoration:none;color:inherit}
.main-nav .active{background:var(--nav-active);color:var(--orange);width:77px;text-align:center}
.rule{left:0;top:116px;width:1047px;height:5px;background:var(--orange)}

/* hero */
.hero{left:0;top:121px;width:1047px;height:273px;background:linear-gradient(90deg,#f4f4f4 0%,#ececec 85%,#c4c4c4 100%)}
.hero-photo{left:0;top:0;width:545px;height:273px;background:linear-gradient(180deg,#e8e8e8,#d6d6d6)}
.hero-title{left:590px;top:54px;font-size:44px;color:var(--ink)}
.hero-sub{left:591px;top:108px;width:360px;font-size:20px;line-height:22px;color:var(--orange)}
.btn{left:589px;top:185px;width:114px;height:39px;background:var(--orange);border-bottom:3px solid #c98d00;color:var(--ink);font-size:22px;text-align:center;line-height:37px;text-decoration:none}

/* features */
.feature{top:425px;width:300px;height:230px;padding:0 16px;text-align:center}
.feature.is-highlight{background:var(--orange);color:var(--white)}
.feature svg{margin-top:24px;height:50px}
.feature h3{font-size:26px;color:var(--ink);margin-top:22px;line-height:30px}
.feature.is-highlight h3{color:var(--white)}
.feature p{text-align:left;font-size:11.5px;line-height:20px;margin-top:10px}

/* intro band */
.band{left:0;top:673px;width:1047px;height:309px;background:var(--grey-band)}
.section-title{font-size:24px;color:var(--orange);line-height:28px}
.welcome-photo{left:87px;width:228px;height:151px;background:linear-gradient(135deg,#9aa6b0,#c9b49a 60%,#e0a060)}
.copy{font-size:11.5px;line-height:20px;color:#444;letter-spacing:.4px}
.copy-narrow{font-size:11px;letter-spacing:.1px;height:160px;overflow:hidden}
.copy-wide{font-size:11px;letter-spacing:.15px}

/* footer */
.footer{left:0;top:982px;width:1047px;height:218px;background:var(--footer)}
.foot-nav{left:94px;top:10px;font-size:13px;font-weight:700;color:var(--white);line-height:27.3px;list-style:none}
.foot-nav .active{color:var(--orange)}
.contact{left:385px;top:20px;color:var(--white);font-size:13px;font-weight:700;line-height:27.3px}
.social{width:41px;height:41px;border:2px solid var(--orange);border-radius:50%;color:var(--white);font-size:10px;font-weight:700;text-align:center;line-height:37px}
.social.is-filled{background:var(--orange);color:var(--ink)}
.legal{left:0;top:1163px;width:1047px;border-top:1px solid #555;height:37px;text-align:center;font-size:11px;line-height:36px;color:var(--orange)}
.legal b{color:var(--white)}
</style>
</head>
<body>

<header>
  <div class="abs brand">
    <div class="brand-mark">KWR</div>
    <div class="brand-divider"></div>
    <div class="brand-name">
      <div class="l1">Keystone Works</div>
      <div class="l2">Development Limited</div>
      <div class="l3">TRANSFORMING YOUR VISION INTO REALITY</div>
    </div>
  </div>
  <nav class="abs main-nav">
    <a class="active" href="#">HOME</a>
    <a href="#" style="margin-left:24px">ABOUT</a>
    <a href="#" style="margin-left:42px">EXPERTISE</a>
    <a href="#" style="margin-left:34px">SULOTIONS</a>
    <a href="#" style="margin-left:40px">INDUSTRIES</a>
  </nav>
  <div class="abs rule"></div>
</header>

<section class="abs hero">
  <div class="abs hero-photo" role="img" aria-label="Business people assembling large white jigsaw puzzle pieces"></div>
  <h1 class="abs hero-title display">PMO SERVICES</h1>
  <p class="abs hero-sub display">Improve the performance of your projects, programs and portfolios by implementing effective best practices, governance and control.</p>
  <a class="abs btn display" href="#">READ MORE</a>
</section>

<section>
  <div class="abs feature" style="left:71px">
    <svg viewBox="0 0 50 50" width="50" aria-hidden="true">
      <rect x="19" y="0" width="12" height="10" fill="#111"/>
      <rect x="24" y="10" width="2" height="9" fill="#111"/>
      <rect x="5" y="19" width="40" height="2" fill="#111"/>
      <rect x="5" y="19" width="2" height="10" fill="#111"/><rect x="24" y="19" width="2" height="10" fill="#111"/><rect x="43" y="19" width="2" height="10" fill="#111"/>
      <rect x="0" y="28" width="12" height="10" fill="#111"/><rect x="14" y="28" width="10" height="10" fill="#111"/><rect x="26" y="28" width="10" height="10" fill="#111"/><rect x="38" y="28" width="12" height="10" fill="#111"/>
    </svg>
    <h3 class="display">STRUCTURE</h3>
    <p>Lorem Ipsum is simply dummy text of the printing and typesetting industry. Lorem Ipsum has been the industry's standard dummy text ever since the 1500s, when Lorem Ipsum is simply dummy text...</p>
  </div>
  <div class="abs feature is-highlight" style="left:371px">
    <svg viewBox="0 0 50 50" width="50" aria-hidden="true">
      <rect x="7" y="2" width="16" height="7" rx="3" fill="#fff"/>
      <rect x="14" y="9" width="2" height="6" fill="#fff"/>
      <polygon points="15,15 25,23 15,31 5,23" fill="#fff"/>
      <rect x="25" y="22" width="10" height="2" fill="#fff"/>
      <rect x="35" y="19" width="12" height="8" rx="4" fill="#fff"/>
      <rect x="14" y="31" width="2" height="6" fill="#fff"/>
      <polygon points="9,37 23,37 21,45 7,45" fill="#fff"/>
    </svg>
    <h3 class="display">PROCESSES</h3>
    <p>Lorem Ipsum is simply dummy text of the printing and typesetting industry. Lorem Ipsum has been the industry's standard dummy text ever since the 1500s, when Lorem Ipsum is simply dummy text...</p>
  </div>
  <div class="abs feature" style="left:671px">
    <svg viewBox="0 0 50 50" width="50" aria-hidden="true">
      <circle cx="25" cy="21" r="15" fill="none" stroke="#111" stroke-width="3"/>
      <ellipse cx="25" cy="21" rx="7" ry="15" fill="none" stroke="#111" stroke-width="2"/>
      <line x1="10" y1="21" x2="40" y2="21" stroke="#111" stroke-width="2"/>
      <path d="M13 10 A18 18 0 0 0 37 36" fill="none" stroke="#111" stroke-width="2"/>
      <rect x="24" y="38" width="2" height="6" fill="#111"/>
      <rect x="17" y="44" width="16" height="3" fill="#111"/>
    </svg>
    <h3 class="display">EXPERTISE</h3>
    <p>Lorem Ipsum is simply dummy text of the printing and typesetting industry. Lorem Ipsum has been the industry's standard dummy text ever since the 1500s, when Lorem Ipsum is simply dummy text...</p>
  </div>
</section>

<section class="abs band">
  <h2 class="abs section-title display" style="left:88px;top:16px">WELCOME TO KWR KEYSTONE WORKS</h2>
  <div class="abs welcome-photo" style="top:56px" role="img" aria-label="Team of colleagues meeting around an office table"></div>
  <p class="abs copy copy-narrow" style="left:325px;top:52px;width:197px">Lorem Ipsum is simply dummy text of the printing and typesetting industry. Lorem Ipsum has been the industry's standard dummy text ever since the 1500s, when an unknown printer took a galley of type and scrambled it to make a type specimen book. It has survived not</p>
  <p class="abs copy copy-wide" style="left:88px;top:220px;width:436px">only five centuries, but also the leap into electronic typesetting, remaining essentially unchanged. Itwas popularised in the 1960s with the release of Letraset sheets containing Lorem Ipsum passages, and more recently with desktop...</p>

  <h2 class="abs section-title display" style="left:548px;top:16px">SERVICE STRENGTHS</h2>
  <p class="abs copy" style="left:550px;top:55px;width:416px">Lorem Ipsum is simply dummy text of the printing and typesetting industry. Lorem Ipsum has been the industry's standard dummy text ever since the 1500s, when an unknown printer took a galley of type and scrambled it to make a type specimen book. It has survived not only five centuries...</p>
  <h2 class="abs section-title display" style="left:548px;top:162px">CUSTOMER EXPERIENCE</h2>
  <p class="abs copy" style="left:550px;top:200px;width:416px">Lorem Ipsum is simply dummy text of the printing and typesetting industry. Lorem Ipsum has been the industry's standard dummy text ever since the 1500s, when an unknown printer took a galley of type and scrambled it to make a type specimen book. It has survived not only five centuries...</p>
</section>

<footer class="abs footer">
  <ul class="abs foot-nav">
    <li class="active">HOME</li><li>ABOUT</li><li>EXPERTISE</li><li>SULOTIONS</li><li>INDUSTRIES</li><li>CONTACT</li>
  </ul>
  <h2 class="abs section-title display" style="left:385px;top:8px">CONTACT WITH US</h2>
  <div class="abs contact" style="top:32px">
    Office No., Building Name,<br>Area, Near Area,<br>City, State, Country<br>Call : +44 120 555 0148<br>Email : info@kwrKeystoneWorks
  </div>
  <h2 class="abs section-title display" style="left:694px;top:8px">FOLLOW US ON :</h2>
  <div class="abs social is-filled" style="left:694px;top:52px">Feed</div>
  <div class="abs social" style="left:765px;top:52px">Post</div>
  <div class="abs social" style="left:835px;top:52px">Work</div>
  <div class="abs social" style="left:905px;top:52px">Chat</div>
  <div class="abs social" style="left:694px;top:116px">Plus</div>
  <div class="abs social" style="left:765px;top:116px">Pins</div>
  <div class="abs social" style="left:835px;top:116px">Clip</div>
  <div class="abs social" style="left:905px;top:116px">Grid</div>
</footer>
<div class="abs legal">© <b>KWRKeystoneWorks</b> - 2014. All Rights Reserved. <b>Privacy Policy.</b></div>

</body>
</html>
```